my personal cards just intrducing my self

Massage Therapy to get my name out their

Target Market(s)

40 year olds who enjoy massage

Industry/Entity Type

Massage

Contact Information for Business Card

Marcus L Tolhaven
LMT-Licensed Massage Therapist
*Swedish *Deep Tissue *Prenatal
*Reflexology *Chair and more

(738)-462-1937
marcustolhaven@mailbrook.net

Font styles to use
Serif

Colors
0456a4
6b449b

```html
<!DOCTYPE html>
<html lang="en">
<head>
<meta charset="utf-8">
<title>Marcus L Tolhaven – Business Card</title>
<link href="https://fonts.googleapis.com/css2?family=Open+Sans:wght@300;400;600&display=swap" rel="stylesheet">
<style>
  :root {
    --blue: #0456a4;
    --blue-bright: #0a6fc9;
    --purple: #6b449b;
    --purple-light: #8a63b3;
    --lavender: #a9b6e0;
    --white: #ffffff;
    --backdrop: #e4e4e6;
  }
  * { margin: 0; padding: 0; box-sizing: border-box; }
  html, body { width: 1200px; height: 1000px; overflow: hidden; }
  body {
    background: var(--backdrop);
    font-family: "Open Sans", Arial, sans-serif;
    position: relative;
  }
  .card {
    position: absolute;
    width: 560px;
    height: 320px;
    background: var(--white);
    border-radius: 26px;
    overflow: hidden;
    box-shadow: 0 6px 18px rgba(0,0,0,0.12);
  }
  .card--front { left: 120px; top: 110px; }
  .card--back { left: 520px; top: 570px; }

  /* front */
  .front-band { position: absolute; height: 26px; background: var(--blue-bright); }
  .front-band::after { content: ""; position: absolute; left: 0; right: 0; height: 8px; background: var(--blue); }
  .front-band--top { left: 70px; width: 380px; top: 0; }
  .front-band--top::after { bottom: 0; }
  .front-band--bottom { left: 210px; width: 350px; bottom: 0; }
  .front-band--bottom::after { top: 0; }
  .front-identity {
    position: absolute; left: 150px; top: 120px;
    display: flex; align-items: center; gap: 14px;
  }
  .mark {
    width: 66px; height: 66px; border-radius: 50%;
    background: var(--purple); color: var(--white);
    display: flex; align-items: center; justify-content: center;
    font-weight: 600; font-size: 18px;
  }
  .front-name { color: var(--purple); font-size: 25px; font-weight: 600; line-height: 1.1; }
  .front-title { color: var(--lavender); font-size: 19px; font-weight: 300; }

  /* back */
  .back-panel { position: absolute; left: 300px; width: 200px; top: 0; height: 320px; background: var(--purple); }
  .back-panel__top { position: absolute; left: 0; right: 0; top: 0; height: 100px; background: var(--purple-light); display: flex; align-items: center; justify-content: center; }
  .back-panel .mark { width: 58px; height: 58px; background: var(--white); color: var(--purple); font-size: 16px; }
  .services { position: absolute; left: 22px; top: 112px; list-style: none; color: var(--white); font-size: 18px; line-height: 1.2; }
  .services li::before { content: ""; display: inline-block; width: 9px; height: 9px; border-radius: 50%; background: var(--white); margin-right: 7px; vertical-align: 2px; }
  .name-band {
    position: absolute; left: 0; width: 300px; top: 88px; height: 64px;
    background: var(--blue-bright); padding: 6px 16px;
  }
  .name-band__name { color: var(--white); font-size: 22px; font-weight: 600; line-height: 1.15; white-space: nowrap; }
  .name-band__title { color: var(--lavender); font-size: 17px; font-weight: 400; }
  .contact-band {
    position: absolute; left: 0; right: 0; top: 236px; height: 56px;
    background: var(--blue);
    display: flex; align-items: center; justify-content: space-between;
    padding: 0 20px; color: var(--white); font-weight: 600; font-size: 16px;
  }
  .contact { display: flex; align-items: center; gap: 7px; }
  .contact svg { width: 18px; height: 18px; fill: var(--white); }
  .back-foot { position: absolute; left: 300px; width: 200px; top: 292px; height: 28px; background: var(--purple); }
</style>
</head>
<body>
  <section class="card card--front" aria-label="Business card front">
    <div class="front-band front-band--top"></div>
    <div class="front-band front-band--bottom"></div>
    <div class="front-identity">
      <div class="mark">MLT</div>
      <div>
        <p class="front-name">Marcus L Tolhaven</p>
        <p class="front-title">Licensed Massage Therapist</p>
      </div>
    </div>
  </section>

  <section class="card card--back" aria-label="Business card back">
    <div class="back-panel">
      <div class="back-panel__top"><div class="mark">MLT</div></div>
      <ul class="services">
        <li>Swedish</li>
        <li>Deep Tissue</li>
        <li>Prenatal</li>
        <li>Reflexology</li>
        <li>Chair and more</li>
      </ul>
    </div>
    <div class="name-band">
      <p class="name-band__name">Marcus L Tolhaven</p>
      <p class="name-band__title">Licensed Massage Therapist</p>
    </div>
    <div class="contact-band">
      <span class="contact">
        <svg viewBox="0 0 24 24" aria-hidden="true"><path d="M6.6 10.8a15 15 0 0 0 6.6 6.6l2.2-2.2a1 1 0 0 1 1-.25 11.4 11.4 0 0 0 3.6.57 1 1 0 0 1 1 1V20a1 1 0 0 1-1 1A17 17 0 0 1 3 4a1 1 0 0 1 1-1h3.5a1 1 0 0 1 1 1c0 1.25.2 2.45.57 3.57a1 1 0 0 1-.25 1z"/></svg>
        (738)-462-1937
      </span>
      <span class="contact">
        <svg viewBox="0 0 24 24" aria-hidden="true"><path d="M2 5h20v14H2z M2 5l10 8 10-8" fill="none" stroke="#fff" stroke-width="2"/></svg>
        marcustolhaven@mailbrook.net
      </span>
    </div>
    <div class="back-foot"></div>
  </section>
</body>
</html>
```